Bakery Business Cards

We are in need of business cards for our bakery business--something non-generic that reflects our business and will stand out. We are a wholesale bakery that primarily services in-store bakeries, casinos, schools, distributors, and fund-raising companies. The family business was founded in 1960. (www.marlowsovenworks.com)

```html
<!DOCTYPE html>
<html lang="en">
<head>
<meta charset="utf-8">
<title>Marlow's Ovenworks — Business Cards</title>
<link rel="stylesheet" href="https://fonts.googleapis.com/css2?family=Lato:wght@400;700&family=Dancing+Script:wght@600&display=swap">
<style>
  :root {
    --bg: #c9c9c9;
    --bg-light: #dedede;
    --brand-blue: #2348a0;
    --brand-blue-deep: #1d3c8a;
    --cream: #f4ede4;
    --peach: #e8cfae;
    --berry: #c98a86;
    --white: #ffffff;
  }
  * { box-sizing: border-box; margin: 0; padding: 0; }
  html, body { width: 1200px; height: 804px; overflow: hidden; }
  body {
    background: radial-gradient(ellipse at 50% 40%, var(--bg-light), var(--bg) 75%);
    font-family: "Lato", sans-serif;
    position: relative;
  }
  .card {
    position: absolute;
    top: 259px;
    width: 500px;
    height: 286px;
    overflow: hidden;
    box-shadow: 0 18px 40px rgba(0,0,0,0.22);
  }
  .card--back { left: 70px; background: var(--brand-blue); }
  .card--front { left: 630px; background: var(--cream); }

  .photo { position: absolute; inset: 0; }
  .card--back .photo {
    background: radial-gradient(circle at 25% 30%, #5d74b4 0 18%, transparent 19%),
                radial-gradient(circle at 78% 75%, #4f68ab 0 16%, transparent 17%),
                linear-gradient(135deg, #3b58a6, var(--brand-blue) 60%, #2c4ea0);
  }
  .card--front .photo {
    bottom: 92px;
    background: radial-gradient(circle at 14% 30%, var(--peach) 0 14%, transparent 15%),
                radial-gradient(circle at 82% 55%, #efe2d2 0 20%, transparent 21%),
                radial-gradient(circle at 30% 85%, var(--berry) 0 10%, transparent 11%),
                linear-gradient(160deg, #f7f1ea, var(--cream));
    opacity: 0.9;
  }

  .brand {
    position: absolute;
    left: 0; right: 0;
    text-align: center;
  }
  .brand__name {
    display: block;
    font-weight: 700;
    font-size: 38px;
    letter-spacing: 1px;
    line-height: 1;
  }
  .brand__since {
    display: block;
    font-size: 11px;
    letter-spacing: 3px;
    margin-top: 6px;
  }
  .card--back .brand { top: 92px; color: var(--white); }
  .card--front .brand { top: 38px; color: var(--brand-blue); }

  .website {
    position: absolute;
    left: 0; right: 0; top: 200px;
    text-align: center;
    color: var(--white);
    font-size: 13px;
    letter-spacing: 5px;
  }

  .tagline {
    position: absolute;
    left: 0; right: 0; top: 120px;
    text-align: center;
    font-family: "Dancing Script", cursive;
    font-size: 24px;
    color: var(--brand-blue);
  }

  .contact-band {
    position: absolute;
    left: 0; right: 0; bottom: 0;
    height: 92px;
    background: var(--brand-blue);
    color: var(--white);
  }
  .contact-list {
    list-style: none;
    position: absolute;
    left: 22px; top: 16px;
    font-size: 13px;
    line-height: 20px;
  }
  .contact-list li { display: flex; align-items: center; gap: 9px; }
  .contact-list svg { width: 13px; height: 13px; flex: none; }

  .partner-badge {
    position: absolute;
    right: 22px; top: 8px;
    width: 76px; height: 76px;
    border-radius: 50%;
    border: 3px solid var(--white);
  }
</style>
</head>
<body>

<section class="card card--back">
  <div class="photo" role="img" aria-label="Overhead photo of pies and baked goods tinted in brand blue"></div>
  <div class="brand">
    <span class="brand__name">Marlow's Ovenworks</span>
    <span class="brand__since">SINCE 1960</span>
  </div>
  <p class="website">www.marlowsovenworks.com</p>
</section>

<section class="card card--front">
  <div class="photo" role="img" aria-label="Soft photo of fruit pies and pastries on plates"></div>
  <div class="brand">
    <span class="brand__name">Marlow's Ovenworks</span>
    <span class="brand__since">SINCE 1960</span>
  </div>
  <p class="tagline">Serving Sweetness, Since 1960</p>

  <div class="contact-band">
    <ul class="contact-list">
      <li>
        <svg viewBox="0 0 16 16" aria-hidden="true"><circle cx="8" cy="8" r="8" fill="#fff"/><path d="M5 4.5l1.6-.4 1 2-1 .8a5 5 0 0 0 2.5 2.5l.8-1 2 1-.4 1.6c-3.6.3-6.8-2.9-6.5-6.5z" fill="#2348a0"/></svg>
        (405) 555-0142
      </li>
      <li>
        <svg viewBox="0 0 16 16" aria-hidden="true"><circle cx="8" cy="8" r="8" fill="#fff"/><rect x="4" y="5.2" width="8" height="5.6" fill="#2348a0"/><path d="M4 5.2l4 3 4-3" stroke="#fff" stroke-width="0.9" fill="none"/></svg>
        sales@marlowsovenworks.com
      </li>
      <li>
        <svg viewBox="0 0 16 16" aria-hidden="true"><circle cx="8" cy="8" r="8" fill="#fff"/><path d="M8 3.5a3 3 0 0 0-3 3c0 2.2 3 6 3 6s3-3.8 3-6a3 3 0 0 0-3-3z" fill="#2348a0"/><circle cx="8" cy="6.5" r="1.1" fill="#fff"/></svg>
        1720 Millbrook Ave, Oklahoma City, OK 73107
      </li>
    </ul>
    <div class="partner-badge" role="img" aria-label="Partner membership badge"></div>
  </div>
</section>

</body>
</html>
```